Specialty Plumbing Distributor Advertisement Flyer

We are looking to design a flyer to catch the eye of backflow preventer training schools and instructors and advertise a program we have here. Our company specializes in repair parts, tools, technical assistance etc. and through this no-cost program, we donate educational material to assist trainers for their classes. We offer coupons, store credit and free resources on website. It is called our “Keystone Mentor Scheme” and we also have a page on our website dedicated to the trainers we work with, where we send customers of ours that need backflow schooling.
Target Market(s)
Plumbing Training Schools
Industry/Entity Type
Education

```html
<!DOCTYPE html>
<html lang="en">
<head>
<meta charset="utf-8">
<title>Keystone Mentor Scheme Flyer</title>
<link rel="stylesheet" href="https://fonts.googleapis.com/css2?family=Arimo:wght@400;700&display=swap">
<style>
  :root {
    --backdrop: #3a3a3a;
    --paper: #ffffff;
    --crimson: #dc164b;
    --royal: #3f4fa8;
    --panel-grey: #e6e6e6;
    --ink: #2b2b2b;
    --body-ink: #333333;
  }
  * { box-sizing: border-box; margin: 0; padding: 0; }
  html, body {
    width: 1200px; height: 1200px; overflow: hidden;
    background: var(--backdrop);
    font-family: "Arimo", Arial, sans-serif;
  }
  .flyer {
    position: absolute; left: 223px; top: 107px;
    width: 766px; height: 991px;
    background: var(--paper); overflow: hidden;
  }
  .header { position: absolute; left: 0; top: 0; width: 100%; height: 134px; }
  .brand { position: absolute; left: 35px; top: 36px; display: flex; align-items: center; gap: 62px; }
  .brand-square { width: 56px; height: 56px; background: var(--crimson); }
  .brand-name { color: var(--royal); font-weight: 400; line-height: 1; }
  .brand-name .line-main { display: block; font-size: 37px; }
  .brand-name .line-sub { display: block; font-size: 19px; margin-top: 5px; }

  .title-band { position: absolute; left: 0; top: 134px; width: 100%; height: 292px; background: var(--crimson); }
  .stripe-white { position: absolute; top: 402px; height: 11px; background: var(--paper); }
  .stripe-white.left { left: 0; width: 142px; }
  .stripe-white.right { left: 271px; width: 495px; }
  .stripe-blue { position: absolute; left: 369px; top: 426px; width: 397px; height: 7px; background: var(--royal); }

  .title { position: absolute; left: 40px; top: 169px; color: var(--paper); }
  .title .kicker { display: block; font-size: 50px; font-weight: 400; line-height: 1; }
  .title .headline { display: block; font-size: 74px; font-weight: 700; line-height: 69px; margin-top: -2px; }

  .hero-frame { position: absolute; left: 0; top: 0; width: 766px; height: 400px; }

  .info-panel { position: absolute; left: 0; top: 483px; width: 100%; height: 279px; background: var(--panel-grey); }
  .worker-photo {
    position: absolute; left: 0; top: 357px; width: 361px; height: 634px;
    background: linear-gradient(180deg, #c9ccd8 0%, #6d7fc4 35%, #3a52ad 70%, #2c4296 100%);
  }

  .includes { position: absolute; left: 377px; top: 520px; }
  .includes h2 { font-size: 31px; font-weight: 700; color: var(--royal); letter-spacing: 0.3px; }
  .includes ul { list-style: none; margin-top: 17px; margin-left: 54px; }
  .includes li { position: relative; font-size: 27px; color: var(--body-ink); height: 39px; line-height: 39px; padding-left: 41px; }
  .includes li::before {
    content: ""; position: absolute; left: 0; top: 14px;
    width: 11px; height: 11px; border-radius: 50%; background: var(--crimson);
  }

  .call { position: absolute; left: 358px; top: 805px; width: 408px; text-align: center; }
  .call-label { font-size: 31px; font-weight: 700; color: var(--crimson); letter-spacing: 0.5px; }
  .call-line { display: flex; justify-content: center; align-items: center; gap: 14px; margin-top: 2px; margin-right: 30px; }
  .call-number { font-size: 39px; font-weight: 700; color: var(--ink); }

  .web-bar {
    position: absolute; left: 358px; top: 895px; width: 408px; height: 59px;
    background: var(--royal); border-radius: 5px 0 0 5px;
    color: var(--paper); font-size: 24px; display: flex; align-items: center; justify-content: center;
  }
  .foot-line { position: absolute; left: 358px; top: 985px; width: 408px; height: 6px; background: var(--crimson); }
</style>
</head>
<body>
  <main class="flyer">
    <header class="header">
      <div class="brand">
        <span class="brand-square"></span>
        <span class="brand-name">
          <span class="line-main">Summit Flowguard</span>
          <span class="line-sub">Supply Company</span>
        </span>
      </div>
    </header>

    <section class="title-band"></section>
    <div class="stripe-white left"></div>
    <div class="stripe-white right"></div>
    <div class="stripe-blue"></div>

    <h1 class="title">
      <span class="kicker">KEYSTONE</span>
      <span class="headline">MENTOR<br>SCHEME</span>
    </h1>

    <svg class="hero-frame" viewBox="0 0 766 400" width="766" height="400">
      <defs>
        <linearGradient id="sinkPhotoTone" x1="0" y1="0" x2="1" y2="1">
          <stop offset="0" stop-color="#e9e3e0"/>
          <stop offset="0.6" stop-color="#c9c2c4"/>
          <stop offset="1" stop-color="#2f5fc4"/>
        </linearGradient>
      </defs>
      <polygon points="561,0 398,211 565,382 766,302 766,0" fill="#3f4fa8"/>
      <polygon role="img" aria-label="Photo of a plumber in blue overalls fitting pipes under a sink"
               points="581,0 421,209 573,365 766,297 766,0" fill="url(#sinkPhotoTone)"/>
    </svg>

    <section class="info-panel"></section>

    <div class="worker-photo" role="img" aria-label="Photo of a smiling plumber in blue overalls holding a pipe wrench and hose, wearing a tool belt"></div>

    <section class="includes">
      <h2>PROGRAM INCLUDES:</h2>
      <ul>
        <li>Cover Removal</li>
        <li>Valve Removal</li>
        <li>Seat Removal</li>
        <li>Disc Removal</li>
      </ul>
    </section>

    <section class="call">
      <p class="call-label">CALL NOW</p>
      <div class="call-line">
        <svg width="36" height="36" viewBox="0 0 24 24" aria-hidden="true">
          <path fill="#dc164b" d="M6.6 10.8a15.1 15.1 0 0 0 6.6 6.6l2.2-2.2c.3-.3.7-.4 1-.2 1.1.4 2.3.6 3.6.6.6 0 1 .4 1 1V20c0 .6-.4 1-1 1A17 17 0 0 1 3 4c0-.6.4-1 1-1h3.5c.6 0 1 .4 1 1 0 1.3.2 2.500.6 3.6.1.3 0 .7-.2 1z"/>
        </svg>
        <span class="call-number">800.555.0142</span>
      </div>
    </section>

    <div class="web-bar">www.FlowguardParts.com</div>
    <div class="foot-line"></div>
  </main>
</body>
</html>
```